Bright Sprouts Business Card

speech therapy business card that is fun and professional using my logo.
Updates

Wow wonderful dedigns ... 

Industry/Entity Type

Business

Contact Information for Business Card

Tessa Morvan
Brelow Certified Practising Speech Pathologist
B.Sp.Path MSPAA CPSP
ph: 0413906281
brightsproutsspeechpathology@mailbox.example
www.brightsproutsspeechpathology.example

```html
<!DOCTYPE html>
<html lang="en">
<head>
<meta charset="utf-8">
<title>Bright Sprouts Business Card Concepts</title>
<link href="https://fonts.googleapis.com/css2?family=Arimo:wght@700&family=PT+Sans:ital,wght@0,400;0,700;1,400&display=swap" rel="stylesheet">
<style>
:root{
  --plum:#9b2f5c;
  --sky:#1e88c4;
  --white:#ffffff;
  --ink-bg:#000000;
  --name-font:"Arimo", Arial, sans-serif;
  --body-font:"PT Sans", Arial, sans-serif;
}
*{box-sizing:border-box;margin:0;padding:0}
html,body{width:1132px;height:1200px;overflow:hidden;background:var(--ink-bg)}
.sheet{position:absolute;left:0;top:0;width:1047px;height:1110px;transform:scale(1.0812,1.0811);transform-origin:0 0}
.card{position:absolute;width:354px;height:205px;overflow:hidden;background:var(--white);font-family:var(--body-font)}
.card > *{position:absolute}
.card svg.bg{left:0;top:0;width:354px;height:205px}
.card-a{left:100px;top:80px}
.card-b{left:544px;top:80px;background:var(--plum)}
.card-c{left:100px;top:326px}
.card-d{left:544px;top:326px}
.card-e{left:100px;top:567px}
.card-f{left:544px;top:567px}
.card-g{left:310px;top:809px}

.holder-name{font-family:var(--name-font);font-weight:700;font-size:16.5px;color:var(--white);white-space:nowrap}
.credential{font-style:italic;font-size:10.5px;color:var(--white);white-space:nowrap}
.contact{font-size:9px;line-height:12px;color:var(--white);white-space:nowrap}
.contact.small{font-size:8.2px;line-height:10.2px}
.contact.plum{color:var(--plum)}
.contact.sky{color:var(--sky)}

.brand{display:flex;flex-direction:column;align-items:center;gap:5px;width:120px}
.brand-dot{width:22px;height:22px;border-radius:50%;background:var(--sky)}
.brand-name{font-family:var(--body-font);font-weight:700;font-size:15px;color:var(--sky);white-space:nowrap}

/* card a */
.card-a .holder-name{left:14px;top:41px}
.card-a .credential{left:14px;top:70px}
.card-a .contact{left:14px;top:136px;font-size:8.5px}
.card-a .brand{left:227px;top:110px}
/* card b */
.card-b .brand{left:116px;top:40px}
.card-b .holder-name{left:18px;top:129px;color:var(--plum)}
.card-b .contact{left:144px;top:121px}
.card-b .credential{left:18px;top:172px}
/* card c */
.card-c .holder-name{left:154px;top:41px}
.card-c .credential{left:14px;top:70px;color:var(--plum)}
.card-c .contact{left:149px;top:136px}
.card-c .brand{left:12px;top:112px}
/* card d */
.card-d .brand{left:116px;top:30px}
.card-d .holder-name{left:14px;top:136px}
.card-d .contact{left:163px;top:131px}
.card-d .credential{left:12px;top:171px;font-style:normal;font-size:10px}
/* card e */
.card-e .holder-name{left:0;width:342px;text-align:center;top:53px}
.card-e .credential{left:14px;top:86px}
.card-e .brand{left:16px;top:122px}
.card-e .contact{left:149px;top:150px}
/* card f */
.card-f .brand{left:17px;top:82px}
.card-f .holder-name{left:129px;top:36px;font-size:15px}
.card-f .credential{left:129px;top:58px;font-style:normal;font-size:10px;line-height:13px}
.card-f .contact{left:168px;top:150px}
/* card g */
.card-g .brand{left:167px;top:48px}
.card-g .credential{left:16px;top:139px;color:var(--plum);font-size:10px}
.card-g .holder-name{left:16px;top:163px}
.card-g .contact{left:166px;top:159px}
</style>
</head>
<body>
<main class="sheet">

  <article class="card card-a">
    <svg class="bg" viewBox="0 0 354 205" aria-hidden="true">
      <path d="M0 32 H203 a12 12 0 0 1 12 12 V175 a12 12 0 0 1 -12 12 H0 Z" fill="var(--plum)"/>
      <rect x="0" y="68" width="354" height="17" fill="var(--sky)"/>
    </svg>
    <h2 class="holder-name">Tessa Morvan</h2>
    <p class="credential">Brelow Certified Practising Speech Pathologist&nbsp; B. Sp. Path, MSPAA, CPSP</p>
    <p class="contact">phone: 0413906281<br>brightsproutsspeechpathology@mailbox.example<br>www.brightsproutsspeechpathology.example</p>
    <div class="brand"><span class="brand-dot"></span><span class="brand-name">Bright Sprouts</span></div>
  </article>

  <article class="card card-b">
    <svg class="bg" viewBox="0 0 354 205" aria-hidden="true">
      <rect x="0" y="112" width="354" height="2" fill="var(--white)"/>
      <rect x="0" y="117" width="354" height="43" fill="var(--white)"/>
      <rect x="0" y="163" width="354" height="1.5" fill="var(--white)"/>
      <circle cx="176" cy="62" r="58" fill="none" stroke="var(--white)" stroke-width="1.5"/>
      <circle cx="176" cy="62" r="54" fill="var(--white)"/>
    </svg>
    <div class="brand"><span class="brand-dot"></span><span class="brand-name">Bright Sprouts</span></div>
    <h2 class="holder-name">Tessa Morvan</h2>
    <p class="contact sky">phone: 0413906281<br>brightsproutsspeechpathology@mailbox.example<br>www.brightsproutsspeechpathology.example</p>
    <p class="credential">Brelow Certified Practising Speech Pathologist B. Sp. Path, MSPAA, CPSP</p>
  </article>

  <article class="card card-c">
    <svg class="bg" viewBox="0 0 354 205" aria-hidden="true">
      <path d="M152 32 H354 V187 H152 a12 12 0 0 1 -12 -12 V44 a12 12 0 0 1 12 -12 Z" fill="var(--plum)"/>
      <rect x="0" y="68" width="354" height="17" fill="var(--white)"/>
    </svg>
    <h2 class="holder-name">Tessa Morvan</h2>
    <p class="credential">Brelow Certified Practising Speech Pathologist&nbsp; B. Sp. Path, MSPAA, CPSP</p>
    <div class="brand"><span class="brand-dot"></span><span class="brand-name">Bright Sprouts</span></div>
    <p class="contact">phone: 0413906281<br>brightsproutsspeechpathology@mailbox.example<br>www.brightsproutsspeechpathology.example</p>
  </article>

  <article class="card card-d">
    <svg class="bg" viewBox="0 0 354 205" aria-hidden="true">
      <rect x="0" y="0" width="155" height="205" fill="var(--sky)"/>
      <circle cx="188" cy="32" r="100" fill="var(--sky)"/>
      <circle cx="176" cy="30" r="88" fill="var(--white)"/>
      <rect x="155" y="125" width="199" height="41" fill="var(--white)"/>
      <rect x="0" y="166" width="354" height="24" fill="var(--sky)"/>
    </svg>
    <div class="brand"><span class="brand-dot"></span><span class="brand-name">Bright Sprouts</span></div>
    <h2 class="holder-name">Tessa Morvan</h2>
    <p class="contact small sky">phone: 0413906281<br>brightsproutsspeechpathology@mailbox.example<br>www.brightsproutsspeechpathology.example</p>
    <p class="credential">Brelow Certified Practising Speech Pathologist B. Sp. Path, MSPAA, CPSP</p>
  </article>

  <article class="card card-e">
    <svg class="bg" viewBox="0 0 354 205" aria-hidden="true">
      <rect x="0" y="0" width="354" height="80" fill="var(--plum)"/>
      <rect x="0" y="80" width="354" height="23" fill="var(--sky)"/>
    </svg>
    <h2 class="holder-name">Tessa Morvan</h2>
    <p class="credential">Brelow Certified Practising Speech Pathologist&nbsp; B. Sp. Path, MSPAA, CPSP</p>
    <div class="brand"><span class="brand-dot"></span><span class="brand-name">Bright Sprouts</span></div>
    <p class="contact plum">phone: 0413906281<br>brightsproutsspeechpathology@mailbox.example<br>www.brightsproutsspeechpathology.example</p>
  </article>

  <article class="card card-f">
    <svg class="bg" viewBox="0 0 354 205" aria-hidden="true">
      <rect x="156" y="132" width="198" height="73" fill="var(--sky)"/>
      <rect x="184" y="0" width="170" height="205" fill="var(--sky)"/>
      <circle cx="198" cy="52" r="82" fill="var(--sky)"/>
      <path d="M160 132 Q215 142 248 98" fill="none" stroke="var(--white)" stroke-width="3"/>
    </svg>
    <div class="brand"><span class="brand-dot"></span><span class="brand-name">Bright Sprouts</span></div>
    <h2 class="holder-name">Tessa Morvan</h2>
    <p class="credential">Brelow Certified Practising Speech Pathologist<br>B. Sp. Path, MSPAA, CPSP</p>
    <p class="contact small">phone: 0413906281<br>brightsproutsspeechpathology@mailbox.example<br>www.brightsproutsspeechpathology.example</p>
  </article>

  <article class="card card-g">
    <svg class="bg" viewBox="0 0 354 205" aria-hidden="true">
      <rect x="0" y="134" width="354" height="1.5" fill="var(--plum)"/>
      <circle cx="227" cy="72" r="72" fill="var(--plum)"/>
      <circle cx="227" cy="72" r="62" fill="var(--white)"/>
      <rect x="0" y="136" width="354" height="18" fill="var(--white)"/>
      <rect x="0" y="155" width="354" height="50" fill="var(--plum)"/>
    </svg>
    <div class="brand"><span class="brand-dot"></span><span class="brand-name">Bright Sprouts</span></div>
    <p class="credential">Brelow Certified Practising Speech Pathologist B. Sp. Path, MSPAA, CPSP</p>
    <h2 class="holder-name">Tessa Morvan</h2>
    <p class="contact small">phone: 0413906281<br>brightsproutsspeechpathology@mailbox.example<br>www.brightsproutsspeechpathology.example</p>
  </article>

</main>
</body>
</html>
```